VELOQUARD Stationery Design Project

I want a stationery design for a web development company consists of:
1- business card
2- Letter Head
3- small Envelope
4- Large Envelope

need a very clean professional simple design yet creative,

The company logo is attached
http://www.artpitchly.com/project-progress/designs.aspx?briefId=5173048&submissionId=73920416

logo font is sui generis rg (attached)
I would like to have the stationery text font to be helvetica font regular or light (can be changed)

I love the combination of cyan, black and grey colors
( will attach some recommended styles)

Industry/Entity Type

Business

Requirements
Should not have
• curves or waves

```html
<!DOCTYPE html>
<html lang="en">
<head>
<meta charset="utf-8">
<title>VELOQUARD Business Card</title>
<link href="https://fonts.googleapis.com/css2?family=Arimo:wght@400;700&display=swap" rel="stylesheet">
<style>
  :root {
    --backdrop: #ebebeb;
    --card-white: #fafafa;
    --card-black: #0b0b0b;
    --gold: #c6a44c;
    --grey-dark: #555555;
    --grey-mid: #8c8c8c;
    --grey-light: #a8a8a8;
  }
  * { margin: 0; padding: 0; box-sizing: border-box; }
  html, body {
    width: 1200px;
    height: 770px;
    overflow: hidden;
    background: var(--backdrop);
    font-family: "Arimo", Helvetica, Arial, sans-serif;
  }
  .stage {
    position: relative;
    width: 1200px;
    height: 770px;
  }
  .card {
    position: absolute;
    top: 242px;
    width: 500px;
    height: 286px;
    box-shadow: 0 6px 18px rgba(0,0,0,0.12);
  }
  .card--front { left: 80px; background: var(--card-white); }
  .card--back  { left: 620px; background: var(--card-black); }

  .brand {
    position: absolute;
    top: 46px;
    left: 44px;
    display: flex;
    align-items: center;
    gap: 14px;
  }
  .brand__square {
    width: 30px;
    height: 30px;
    background: var(--gold);
  }
  .brand__name {
    font-size: 20px;
    font-weight: 400;
    letter-spacing: 7px;
    color: var(--gold);
  }

  .person {
    position: absolute;
    top: 150px;
    left: 44px;
  }
  .person__name {
    font-size: 15px;
    letter-spacing: 1px;
    color: var(--grey-dark);
  }
  .person__role {
    margin-top: 4px;
    font-size: 9px;
    letter-spacing: 1.5px;
    color: var(--grey-light);
  }

  .contact {
    position: absolute;
    top: 196px;
    list-style: none;
    font-size: 10.5px;
    color: var(--grey-mid);
  }
  .contact--lines { left: 160px; }
  .contact--address { left: 318px; }
  .contact li {
    display: flex;
    align-items: flex-start;
    gap: 8px;
    line-height: 17px;
  }
  .contact svg {
    flex: none;
    width: 10px;
    height: 10px;
    margin-top: 3px;
    fill: var(--grey-dark);
  }

  .back-brand {
    position: absolute;
    inset: 0;
    display: flex;
    align-items: center;
    justify-content: center;
    gap: 16px;
  }
  .back-brand__square {
    width: 40px;
    height: 40px;
    background: var(--gold);
  }
  .back-brand__name {
    font-size: 26px;
    font-weight: 400;
    letter-spacing: 8px;
    color: var(--gold);
  }
</style>
</head>
<body>
<main class="stage">

  <section class="card card--front" aria-label="Business card front">
    <div class="brand">
      <span class="brand__square"></span>
      <span class="brand__name">VELOQUARD</span>
    </div>

    <div class="person">
      <p class="person__name">DANIEL HARTLEY</p>
      <p class="person__role">OWNER</p>
    </div>

    <ul class="contact contact--lines">
      <li>
        <svg viewBox="0 0 10 10" aria-hidden="true"><path d="M2 0h2l1 2.5-1.3 1a6 6 0 0 0 2.8 2.8l1-1.3L10 6v2c0 1-1 2-2 2A8 8 0 0 1 0 2c0-1 1-2 2-2z"/></svg>
        <span>555 204 3197</span>
      </li>
      <li>
        <svg viewBox="0 0 10 10" aria-hidden="true"><path d="M0 2h10v6H0z M0.8 2.6 5 5.6 9.2 2.6" fill="none" stroke="#555" stroke-width="1"/></svg>
        <span>hello@veloquard.net</span>
      </li>
      <li>
        <svg viewBox="0 0 10 10" aria-hidden="true"><circle cx="5" cy="5" r="4.4" fill="none" stroke="#555" stroke-width="1"/><path d="M0.6 5h8.8M5 0.6v8.8" stroke="#555" stroke-width="0.8"/></svg>
        <span>www.veloquard.net</span>
      </li>
    </ul>

    <ul class="contact contact--address">
      <li>
        <svg viewBox="0 0 10 10" aria-hidden="true"><path d="M5 0a3.5 3.5 0 0 1 3.5 3.5C8.5 6 5 10 5 10S1.5 6 1.5 3.5A3.5 3.5 0 0 1 5 0zm0 2a1.5 1.5 0 1 0 0 3 1.5 1.5 0 0 0 0-3z"/></svg>
        <span>47 Larch Row St<br>Keller Plaza, NJ 0718</span>
      </li>
    </ul>
  </section>

  <section class="card card--back" aria-label="Business card back">
    <div class="back-brand">
      <span class="back-brand__square"></span>
      <span class="back-brand__name">VELOQUARD</span>
    </div>
  </section>

</main>
</body>
</html>
```